International Travel & Visas Firm needs a Schengen Visa eBook Cover Design

We need an ebook cover design for an online based travel, immigration, visas & nationality law firm called 'OrV' (ordinance and relocation). We are all about helping people overcome the obstacles to travel and ensuring that people achieve their dreams and ambitions through travel to various destinations and bettering their lives.This initial ebook cover is for our downloaded pdf ebook all about Schengen visas and travelling to any of the 26 European countries that form the Schengen Zone.We want people to be excited about buying this book even before receiving it.We would like to see amazing designs that also speak to our logo and new branding.Check out https://ordinanceandrelocation.example/schengen-visas/ and http://ordinanceandrelocation.pages.funnelkit.example/start-your-schengen-visa-application

Target Market(s)

Travellers that want to get a visa to travel around Europe

Industry/Entity Type

Travel Industry

Colors
fbee3d
faa54b

Requirements
Must have
• - Title:
• Schengen Visa Guide
Nice to have
• - tagline:
• Liberate yourself and travel to 26 European Countries
• - OrV Logo
• - Reference to it being an insider's guide to Schengen Visas
• - a play on the word OrV (I am)

```html
<!DOCTYPE html>
<html lang="en">
<head>
<meta charset="utf-8">
<title>Schengen Visa Guide – eBook Cover</title>
<link rel="stylesheet" href="https://fonts.googleapis.com/css2?family=Bebas+Neue&family=Montserrat:wght@300;400&display=swap">
<style>
  :root {
    --stage: #bcb8b7;
    --navy: #172b47;
    --orange: #ea5226;
    --yellow: #f0bb2f;
    --white: #ffffff;
    --land: #e3ddd7;
  }
  html, body {
    margin: 0;
    padding: 0;
    width: 1200px;
    height: 1200px;
    overflow: hidden;
    background: var(--stage);
  }
  .cover {
    position: absolute;
    left: 224px;
    top: 40px;
    width: 752px;
    height: 1120px;
    background: var(--navy);
    overflow: hidden;
  }
  .cover h1 { margin: 0; }
  .title-line {
    position: absolute;
    left: 0;
    width: 100%;
    margin: 0;
    text-align: center;
    font-family: "Bebas Neue", "Oswald", sans-serif;
    font-weight: 400;
    line-height: 1;
  }
  .title-top {
    top: 64px;
    font-size: 112px;
    letter-spacing: -1px;
    color: var(--orange);
  }
  .title-main {
    top: 150px;
    font-size: 300px;
    letter-spacing: -3px;
    color: var(--yellow);
  }
  .tagline {
    position: absolute;
    top: 425px;
    left: 0;
    width: 100%;
    margin: 0;
    text-align: center;
    font-family: "Montserrat", "Helvetica Neue", sans-serif;
    font-weight: 300;
    font-size: 28.5px;
    line-height: 36px;
    color: var(--white);
  }
  .travel-illustration {
    position: absolute;
    left: 75px;
    top: 538px;
    width: 594px;
    height: 392px;
  }
  .author {
    position: absolute;
    top: 966px;
    left: 0;
    width: 100%;
    margin: 0;
    text-align: center;
    font-family: "Bebas Neue", "Oswald", sans-serif;
    font-size: 82px;
    line-height: 1;
    letter-spacing: 3px;
    color: var(--yellow);
  }
</style>
</head>
<body>
  <main class="cover">
    <h1>
      <span class="title-line title-top">Schengen Visa</span>
      <span class="title-line title-main">Guide</span>
    </h1>
    <p class="tagline">Liberate yourself and travel to 26<br>European Countries</p>

    <svg class="travel-illustration" viewBox="0 0 594 392" role="img"
         aria-label="Illustration: world map with planes flying a dashed route around it and a row of famous world landmarks standing on a brown ground line">
      <defs>
        <linearGradient id="scene-tone" x1="0" y1="0" x2="0" y2="1">
          <stop offset="0%" stop-color="var(--land)" stop-opacity="0.18"/>
          <stop offset="55%" stop-color="var(--land)" stop-opacity="0.55"/>
          <stop offset="82%" stop-color="#e9883a" stop-opacity="0.75"/>
          <stop offset="100%" stop-color="#6b4422"/>
        </linearGradient>
      </defs>
      <rect x="0" y="0" width="594" height="392" rx="28" fill="url(#scene-tone)"/>
    </svg>

    <p class="author">Author Name</p>
  </main>
</body>
</html>
```